Webdesign für regionalen Online-Handel
Zielgruppe
Natur pur. Seewil pur.
Online einkaufen auf dem Hof
Mosa Acker ist eine regionale Organisation in Küssnacht am Seewil, welche aus einem Online- & Speditionsteam sowie einigen Produzenten (in den meisten Fällen Bauernhöfe wie Hof Brenzel, Wernohof, die Käserei Tobelmatt, der Bio-Metzgerei Gastrahof oder die Pasta-Manufaktur Livia) besteht.
Die Idee wurde im Rahmen der Corona Krise geboren um die lokalen Produzenten besser mit den Konsumenten zu verbinden und die zum Teil versteckten Perlen der Region in die grosse weite Welt zu tragen.
Dabei möchten wir stets den Gedanken von saisonalen und regionalen Grundstoffen beachten. Sie werden also bei uns keine Erdbeeren im November finden. Dafür aber das Beste was die Seewil Region zu bieten hat. Immer frisch und mit viel Liebe produziert. Zusätzlich unterstützen sie mit jedem Einkauf die Erhaltung einer Tradition welche seit vielen Generationen anhält. Die Bauern, Produzenten und Verarbeiter welche auf dieser Seite ihre Produkte anbieten, sind fair bezahlt und können sich so auf QUALITÄT statt QUANTITÄT konzentrieren.
Aufgabenstellung
Wieso ist MOSA ACKER speziell?
- REGIONAL (Produkte, Produktwahl, CH-Qualität)
- NACHHALTIG (Produktwahl, Grundwerte, Wie wir Business machen, An was Glauben wir, Transparenz)
- PERSÖNLICH (Service, Produktwahl, Qualität, Flexibilität)
Claim / Image
Natur pur. Seewil pur. - Online Hofladen der besten Seewil Produzenten
Die Mosa-Acker Zielgruppe ist eher etwas älter (ca. 35-60) und nicht immer versiert mit Online Stores und Internet. Der Zugang und Auftritt sollte daher sehr einfach sein.
Brand
Der Brand sollte für ehrliche, bodenständige, natürliche sowie nachhaltige Produkte stehen. Im Zentrum stehen die Produzenten sowie die Produkte. Ausserdem sollten der Zugang für alle möglichst einfach sein.
Bildsprache
- Natur
- Ohne grosse Filter
- Produkte
- Produzenten und die Menschen im Hintergrund
- Tiere
Farben
Mosa-Acker soll für Natur, Nachhaltigkeit, Fairness stehen. Die Farbwahl ist daher möglichst Nahe an den Farben eines Waldes während den Jahreszeiten zu wählen. Der Grundauftritt sollte clean und seriös sein.
- Grün
- Braun
- Orange
- Gelb
- Weiss

```html
<!DOCTYPE html>
<html lang="de">
<head>
<meta charset="utf-8">
<title>Mosa Acker – Online Hofladen</title>
<link href="https://fonts.googleapis.com/css2?family=Lato:wght@400;700;900&family=Roboto:wght@400;500&display=swap" rel="stylesheet">
<style>
:root{
  --green:#2d9a3a;
  --green-dark:#1e8a2c;
  --green-btn:#1f902f;
  --text:#333;
  --muted:#555;
  --grey-bg:#f1f1f1;
  --white:#fff;
}
*{box-sizing:border-box;margin:0;padding:0}
html,body{width:1200px;height:4094px;overflow:hidden}
body{font-family:'Lato',sans-serif;color:var(--text);background:var(--white);position:relative}
.abs{position:absolute}
.img{position:absolute;display:block}
.hero-bg{left:0;top:0;width:912px;height:604px;background:linear-gradient(160deg,#3aa845,#218a2d 60%,#2f9c3b)}
.logo{left:112px;top:12px;width:70px;text-align:center;color:var(--white);font-size:10px;letter-spacing:.5px}
.logo i{display:block;width:34px;height:34px;border-radius:50%;background:var(--white);margin:0 auto 6px;opacity:.9}
.nav{left:281px;top:36px;color:var(--white);font-size:13px;font-weight:700}
.nav a{position:absolute;white-space:nowrap;color:inherit;text-decoration:none}
.nav .active::after{content:"";position:absolute;left:0;right:0;top:22px;height:2px;background:var(--white)}
.hero-photo{left:520px;top:84px;width:561px;height:604px;background:linear-gradient(180deg,#3f3a2c 0%,#1e1b14 45%,#e9c32e 70%,#5a7a2a 100%)}
.hero-title{left:114px;top:232px;color:var(--white);font-weight:900;font-size:60px;line-height:54px}
.hero-sub{left:114px;top:352px;width:360px;color:var(--white);font-size:14px;font-weight:700;line-height:18px}
.btn-outline{left:116px;top:434px;width:119px;height:32px;border:2px solid var(--white);border-radius:4px;color:var(--white);font-weight:900;font-size:16px;display:flex;align-items:center;justify-content:center}
.icon-top{top:52px}
.section-title{color:var(--green);font-weight:700;font-size:25px;text-align:center;left:0;width:1200px}
.intro-text{left:170px;top:784px;width:860px;font-size:12.5px;line-height:17.5px;text-align:center;color:var(--text)}
.btn-green{background:var(--green-btn);color:var(--white);font-weight:700;border-radius:20px;display:flex;align-items:center;justify-content:center}
.pill{border:2px solid var(--green);color:var(--green);border-radius:14px;display:flex;align-items:center;justify-content:center;background:var(--white)}
.h2{left:114px;color:var(--green);font-size:24px;font-weight:700}
.row{left:118px;display:flex;gap:38px}
.card{width:213px;position:relative;font-family:'Roboto',sans-serif}
.card .ph{width:213px;height:234px}
.card .name{margin-top:20px;font-size:16px;line-height:19px;color:#222}
.card .price{position:absolute;left:2px;top:326px;font-size:16px;color:#444}
.card .buy{position:absolute;left:120px;top:323px;width:93px;height:21px;font-size:12px;font-family:'Lato',sans-serif}
.arrow{width:14px;height:22px}
.band-yellow{left:116px;top:1432px;width:1084px;height:329px;background:linear-gradient(180deg,#e7cd52,#dcb934 60%,#d2ad2a)}
.band-green{left:0;top:2234px;width:1081px;height:329px;background:linear-gradient(160deg,#36a743,#1f8a2c 55%,#2c9939)}
.band-title{font-weight:900;font-size:35px;line-height:42px}
.band-text{font-weight:700;font-size:16px;line-height:21.5px}
.closing{left:122px;top:3024px;width:955px;text-align:center;font-size:18px;line-height:22px;color:var(--muted);font-family:'Roboto',sans-serif}
.badge{top:3132px;height:48px;border-radius:6px}
.grey{left:0;top:3226px;width:1200px;height:408px;background:var(--grey-bg)}
.tcard{top:3323px;width:482px;height:265px;background:var(--white);border:1px solid #ddd}
.tcard .ph{position:absolute;left:0;top:0;width:233px;height:265px}
.tcard .quote{position:absolute;left:263px;font-size:15px;line-height:21px;color:#222}
.tcard .who{position:absolute;left:263px;font-style:italic;font-size:14px}
.tcard .btn-green{position:absolute;left:263px;width:193px;height:34px;border-radius:3px;font-size:14px;font-weight:400}
.ship{left:100px;top:3675px;width:420px;font-size:10px;line-height:13px;color:#333}
.ship p{margin-bottom:12px}
.brand{font-size:14px;font-weight:700;color:#333;text-align:center;width:100px}
.legal{left:0;top:3814px;width:1200px;height:195px;background:#f6f6f6}
.legal p{width:1020px;margin:0 auto;text-align:center;font-size:10px;line-height:13px;color:#555}
.foot{left:0;top:4009px;width:1200px;height:85px;background:var(--green-dark);color:var(--white);font-size:10px;text-align:center}
</style>
</head>
<body>

<div class="img hero-bg" role="img" aria-label="Grüne Wiese als Hintergrund"></div>
<div class="abs logo"><i></i>MOSA ACKER</div>
<nav class="abs nav">
  <a class="active" style="left:0;top:0">HOME</a>
  <a style="left:77px;top:0">ONLINE HOFLADEN</a>
  <a style="left:239px;top:0">GESCHENKE</a>
  <a style="left:353px;top:0">ÜBER UNS</a>
  <a style="left:453px;top:0">BLOG</a>
  <a style="left:526px;top:0">KONTAKT</a>
</nav>
<svg class="abs icon-top" style="left:1017px" width="14" height="14" viewBox="0 0 14 14"><circle cx="6" cy="6" r="4.5" fill="none" stroke="#bbb" stroke-width="1.6"/><line x1="9.3" y1="9.3" x2="13" y2="13" stroke="#bbb" stroke-width="1.6"/></svg>
<svg class="abs icon-top" style="left:1068px" width="14" height="14" viewBox="0 0 14 14"><path d="M0 1h3l2 8h7l1.5-6H4" fill="none" stroke="#bbb" stroke-width="1.6"/><circle cx="6" cy="12" r="1.3" fill="#bbb"/><circle cx="11" cy="12" r="1.3" fill="#bbb"/></svg>
<div class="img hero-photo" role="img" aria-label="Glas Löwenzahnblüten-Melasse mit gelben Löwenzahnblüten"></div>
<h1 class="abs hero-title">SEEWIL ONLINE<br>HOFLADEN</h1>
<p class="abs hero-sub">Saisonale, regionale und nachhaltige Produkte von den besten Seewil Bauernhöfen</p>
<div class="abs btn-outline">SHOP</div>

<h2 class="abs section-title" style="top:737px">Nachhaltige Top-Qualität direkt von den regionalen Hofläden</h2>
<p class="abs intro-text">Ihr Seewil Online Hofladen mit ausgewählten regionalen, saisonalen und nachhaltigen Produkten. Direkt von den Bauernhöfen, Hofläden sowie den lokalen Produzenten schnell und unkompliziert in die ganze Schweiz und Liechtenstein geliefert. Egal ob für Eigengebrauch, private Geschenke oder Firmengeschenke (Mitarbeitergeschenke, Kundengeschenke, Jubiläumsgutscheine uvm.). Mosa Acker bietet aussergewöhnliche Produkte mit höchster Qualität ohne künstliche Zutaten.</p>
<div class="abs btn-green" style="left:480px;top:883px;width:240px;height:37px;font-size:14px">Erfahren Sie mehr über uns</div>

<h2 class="abs h2" style="top:972px">Empfohlene Produkte</h2>
<div class="abs pill" style="left:976px;top:982px;width:105px;height:22px;font-size:12px">Alle ansehen</div>
<svg class="abs arrow" style="left:79px;top:1133px" viewBox="0 0 14 22"><path d="M11 2L3 11l8 9" fill="none" stroke="#ccc" stroke-width="2"/></svg>
<svg class="abs arrow" style="left:1106px;top:1133px" viewBox="0 0 14 22"><path d="M3 2l8 9-8 9" fill="none" stroke="#ccc" stroke-width="2"/></svg>
<div class="abs row" style="top:1036px">
  <div class="card"><div class="ph" role="img" aria-label="Glas Löwenzahnblüten-Melasse" style="background:linear-gradient(180deg,#2b2a25,#e2c03a 80%)"></div><div class="name">Löwenzahnblüten<br>Melasse - vegan (260g)</div><div class="price">CHF 5.80</div><div class="btn-green buy">Kaufen</div></div>
  <div class="card"><div class="ph" role="img" aria-label="Gläser mit rotem Sirup und Tannenzweigen" style="background:linear-gradient(180deg,#6b6458,#7a2a20 55%,#3e6a2a)"></div><div class="name">Löwenzahnblüten<br>Melasse - vegan (260g)</div><div class="price">CHF 5.80</div><div class="btn-green buy">Kaufen</div></div>
  <div class="card"><div class="ph" role="img" aria-label="Holzkiste mit Hofprodukten" style="background:linear-gradient(180deg,#d8d4cc,#c9a76e 70%,#b8935a)"></div><div class="name">Löwenzahnblüten<br>Melasse - vegan (260g)</div><div class="price">CHF 5.80</div><div class="btn-green buy">Kaufen</div></div>
  <div class="card"><div class="ph" role="img" aria-label="Salami auf einem Holzbrett" style="background:linear-gradient(180deg,#9a8e84,#8a4a38 50%,#b58a5a)"></div><div class="name">Löwenzahnblüten<br>Melasse - vegan (260g)</div><div class="price">CHF 5.80</div><div class="btn-green buy">Kaufen</div></div>
</div>

<div class="img band-yellow" role="img" aria-label="Blühendes Rapsfeld"></div>
<h2 class="abs band-title" style="left:199px;top:1515px;color:#3a3320">Nachhaltige<br>Top-Qualität direkt<br>von den regionalen<br>Hofläden</h2>
<p class="abs band-text" style="left:613px;top:1514px;width:475px;color:#3a3320">Ihr Seewil Online Hofladen mit ausgewählten regionalen, saisonalen und nachhaltigen Produkten. Direkt von den Bauernhöfen, Hofläden sowie den lokalen Produzenten schnell und unkompliziert in die ganze Schweiz und Liechtenstein geliefert. Egal ob für Eigengebrauch, private Geschenke oder Firmengeschenke (Mitarbeitergeschenke, Kundengeschenke, Jubiläumsgutscheine uvm.). Mosa Acker bietet aussergewöhnliche Produkte mit höchster Qualität ohne künstliche Zutaten.</p>

<svg class="abs arrow" style="left:79px;top:1902px" viewBox="0 0 14 22"><path d="M11 2L3 11l8 9" fill="none" stroke="#ccc" stroke-width="2"/></svg>
<svg class="abs arrow" style="left:1106px;top:1902px" viewBox="0 0 14 22"><path d="M3 2l8 9-8 9" fill="none" stroke="#ccc" stroke-width="2"/></svg>
<div class="abs row" style="top:1805px">
  <div class="card"><div class="ph" role="img" aria-label="Wecker" style="background:linear-gradient(180deg,#e9e4dc,#bfb5a5)"></div><div class="name">Nur kurze Zeit</div></div>
  <div class="card"><div class="ph" role="img" aria-label="Geschenkpakete mit Schleifen" style="background:linear-gradient(180deg,#2a2420,#a8261e 55%,#1c2a4a)"></div><div class="name">Gutscheine und Geschenke</div></div>
  <div class="card"><div class="ph" role="img" aria-label="Milch, Käse und Eier" style="background:linear-gradient(180deg,#eef0f2,#d9d6cc 60%,#e8c07a)"></div><div class="name">Käse, Raclette, Fondue<br>und Eier</div></div>
  <div class="card"><div class="ph" role="img" aria-label="Rohe Pouletschenkel in einer Pfanne" style="background:linear-gradient(180deg,#4a2a22,#d9a8a0 55%,#2a2220)"></div><div class="name">Fleischprodukte</div></div>
</div>
<div class="abs pill" style="left:526px;top:2115px;width:147px;height:30px;font-size:16px">Alle ansehen</div>

<div class="img band-green" role="img" aria-label="Grüne Wiese"></div>
<h2 class="abs band-title" style="left:114px;top:2316px;color:var(--white)">Gutscheine und<br>Geschenke</h2>
<p class="abs band-text" style="left:529px;top:2316px;width:470px;color:var(--white)">Egal ob Sie ihre Liebsten, Mitarbeiter oder Kunden für ein Apéro, Geburtstag, Namenstag, Jubiläum, Umzug oder einfach als nette Überraschung beschenken wollen. Finden Sie unter unseren aussergewöhnlichen Produkten etwas für jede Anlass oder warum nicht einfach ein Gutschein von Mosa-Acker. Dieser gibt dem Glücklichen Zugriff auf ein schnell expandierendes Angebot von frischen, nachhaltigen und saisonalen Produkten.</p>

<svg class="abs arrow" style="left:79px;top:2705px" viewBox="0 0 14 22"><path d="M11 2L3 11l8 9" fill="none" stroke="#ccc" stroke-width="2"/></svg>
<svg class="abs arrow" style="left:1106px;top:2705px" viewBox="0 0 14 22"><path d="M3 2l8 9-8 9" fill="none" stroke="#ccc" stroke-width="2"/></svg>
<div class="abs row" style="top:2608px">
  <div class="card"><div class="ph" role="img" aria-label="Gelbe Pralinenschachtel" style="background:linear-gradient(180deg,#e6e6e6,#e0b020 55%,#d8d8d8)"></div><div class="name">Pralinenschachteln ohne<br>Alkohol (3 Pralinen bis 24<br>Pralinen)</div></div>
  <div class="card"><div class="ph" role="img" aria-label="Schwarze Schachtel mit gelber Schleife" style="background:linear-gradient(180deg,#dcdcdc,#2a2a2a 55%,#cfcfcf)"></div><div class="name">Seewil Kirschperlen (6 / 10<br>Pralinen)</div></div>
  <div class="card"><div class="ph" role="img" aria-label="Geschenkkorb mit Bierflaschen" style="background:linear-gradient(180deg,#f0f0f0,#3a2a1a 45%,#8a5a2a)"></div><div class="name">SEEWIL Bier-Körbli (Geschenk)</div></div>
  <div class="card"><div class="ph" role="img" aria-label="Kleiner Geschenkkorb" style="background:linear-gradient(180deg,#f0f0f0,#4a3020 45%,#9a6a38)"></div><div class="name">SEEWIL kleines Geschenk-<br>Körbli</div></div>
</div>
<div class="abs pill" style="left:526px;top:2918px;width:147px;height:30px;font-size:16px">Alle ansehen</div>

<p class="abs closing">Dies ist nur eine kleine Auswahl unserer Käse-, Bio-Fleisch- sowie Geschenkkorb-Spezialitäten, welche bequem von zu Hause in unserem Online Hofladen eingekauft werden können. Gerne stellen wir auch Geschenksets aus allen unseren Bauernhöfen und Hofläden auch auf Wunsch zusammen.</p>

<div class="abs badge" style="left:103px;width:60px;background:#7fbf4a"></div>
<div class="abs badge" style="left:232px;width:50px;background:#2c4a8a"></div>
<div class="abs badge" style="left:361px;width:40px;background:#d9262a"></div>
<div class="abs badge" style="left:504px;width:66px;background:#e0572a"></div>
<div class="abs badge" style="left:640px;width:140px;height:30px;top:3142px;background:#8cc63f"></div>
<div class="abs badge" style="left:835px;width:88px;height:26px;top:3144px;background:#c8a878"></div>
<div class="abs badge" style="left:1017px;width:80px;height:44px;border-radius:22px;border:2px solid #7ab43a;background:var(--white)"></div>

<div class="abs grey"></div>
<h2 class="abs section-title" style="top:3256px;font-size:22px">Unsere Kunden lieben Produkte, Service und Zuverlässigkeit</h2>
<div class="abs" style="left:585px;top:3291px;width:30px;height:3px;background:var(--green)"></div>
<svg class="abs" style="left:46px;top:3436px" width="16" height="26" viewBox="0 0 16 26"><path d="M13 2L3 13l10 11" fill="none" stroke="#2d9a3a" stroke-width="2.5"/></svg>
<svg class="abs" style="left:1138px;top:3436px" width="16" height="26" viewBox="0 0 16 26"><path d="M3 2l10 11-10 11" fill="none" stroke="#2d9a3a" stroke-width="2.5"/></svg>
<div class="abs tcard" style="left:100px">
  <div class="ph" role="img" aria-label="Geöffnete Geschenkbox mit drei Flaschen" style="background:linear-gradient(180deg,#8a8a8a,#e8e8e8 50%,#bdbdbd)"></div>
  <p class="quote" style="top:50px">"Toller Service.<br>Super Produkte, Lieferung<br>perfekt."</p>
  <p class="who" style="top:140px">Frau Bergli</p>
  <div class="btn-green" style="top:176px">Shop entdecken</div>
</div>
<div class="abs tcard" style="left:618px">
  <div class="ph" role="img" aria-label="Käsesortiment in Verpackungen" style="background:linear-gradient(180deg,#6a6a6a,#d8d8d8 55%,#9a9a9a)"></div>
  <p class="quote" style="top:28px">"Wir haben alle Käse erhalten.<br>Alle probiert. Wir sind sehr zu-<br>frieden mit dem Geschmack<br>aller Sorten. Den Büffel Käse<br>haben wir genommen weil<br>keine Lektine in Büffelmilch<br>sind."</p>
  <p class="who" style="top:190px">Frau Tanner</p>
  <div class="btn-green" style="top:218px">Shop entdecken</div>
</div>

<div class="abs ship">
  <p><b>Delivery within 3-4 working days</b></p>
  <p><b>Regional delivery tour free of charge from CHF 150 turnover</b><br>(CHF 0 - 100 = CHF 6.90, CHF 100 - 150 = CHF 2.90)</p>
  <p><b>Other regions in Switzerland free of charge with sales of CHF 200 or more</b><br>(CHF 0 - 60 = CHF 9.90, CHF 60 - 100 = CHF 6.90, CHF 100 - 150 = CHF 3.90,<br>CHF 150 - 200 CHF = CHF 1.90)</p>
</div>
<div class="abs brand" style="left:614px;top:3674px">Zahlblitz</div>
<div class="abs brand" style="left:741px;top:3674px">Geldpost</div>
<div class="abs brand" style="left:841px;top:3674px">Kartova</div>
<div class="abs brand" style="left:930px;top:3674px">Ringkarte</div>
<div class="abs brand" style="left:1021px;top:3674px">Meistra</div>
<svg class="abs" style="left:617px;top:3730px" width="26" height="26" viewBox="0 0 26 26"><path d="M2 13L24 2 17 24l-4-8z" fill="none" stroke="#333" stroke-width="1.6"/><path d="M13 16L24 2" stroke="#333" stroke-width="1.6"/></svg>
<div class="abs" style="left:653px;top:3730px;font-size:11px;line-height:13px;color:#333">Kauf auf<br><span style="color:#d9262a">Rechnung</span></div>
<svg class="abs" style="left:783px;top:3727px" width="26" height="34" viewBox="0 0 26 34"><path d="M13 33C13 33 2 19 2 12a11 11 0 0 1 22 0c0 7-11 21-11 21z" fill="#333"/><circle cx="13" cy="12" r="4.5" fill="#fff"/></svg>
<div class="abs brand" style="left:845px;top:3737px">Bildnetz</div>
<div class="abs brand" style="left:933px;top:3737px">Freundbuch</div>
<div class="abs brand" style="left:1022px;top:3737px">Berufsnetz</div>

<div class="abs legal">
  <p style="margin-top:45px">Mosa-Acker bietet saisonale, regionale, gesunde und nachhaltige Produkte aus der Seewil-Region produziert mit viel Liebe und Handwerkskunst. Natürlich im im Anbau sowie der Herstellung. Der Online Hofladen Webshop enthält auch <u>Bio Produkte mit der Bio Blüte</u>.</p>
  <p style="margin-top:13px">Wir beziehen Produkte von unseren Partnern Wernohof, Hof Brenzel, Dorfkäserei Tobelmatt, Bio Pasta Livia, Bio-Metzgerei Gastrahof, Dolce Vento, Lenas Naschwerk, Bio-Weingut Halden, Gutsbetrieb Sonnmatt und Brauerei Seegold.</p>
  <p style="margin-top:13px"><u>Laktosefreier Käse</u> (<u>Chilli Käse</u>, <u>Heumilch Käse</u>, <u>Büffelkäse</u>, <u>Fondue</u>, <u>Raclette uvm.</u>), <u>Konfitüre / Marmelade</u>, <u>Sirup</u>, <u>Destillate</u> (<u>Absynth</u>, <u>Gin</u>, <u>Träsch</u>, <u>Chrüter</u>, <u>Eierlikör uvm.</u>), <u>Hofbier</u>, <u>Essig</u>, <u>Balsam</u>, <u>Bio Naturkosmetik</u> (<u>Seife in verschiedenen Formen</u>, <u>Deo</u>, <u>Massageöl</u>, <u>Raumspray</u>), <u>Trockenfrüchte</u> (<u>Zwetschgen</u>, <u>Äpfel</u>, <u>Erdbeeren</u>, <u>Dörrbirnen</u>), <u>Apfel Wein</u>, <u>Schaumwein</u>, <u>Salz und Kräuter</u>, <u>Alpaka Wolle uvm.</u></p>
</div>

<footer class="abs foot">
  <p style="margin-top:20px">© 2020 MOSA-ACKER, Wandelhandel GmbH, 6405 Seewilen, Schweiz, info@mosa-acker.ch</p>
  <p style="margin-top:16px">allgemeine Geschäftsbedingungen / Lieferbedingungen / Datenschutz</p>
</footer>

</body>
</html>
```